MES Modul-Struktur grafisch veranschaulichen
Zielgruppe
Wir sind Software-Hersteller. Thema 'MES'. Unsere Kunden sind Produktionsunternehmen.
Mit einem MES (Manufacturing Execution System) werden Produktionsprozesse überwacht, geplant, gesteuert und optimiert. Allgemein geht es darum, die Produktivität zu steigern und Kosten zu minimieren.
Eine MES-Software ist modular strukturiert, so dass der Kunde sich nach Bedarf die einzelnen Funktionsmodule zusammenstellen kann. Unser MES MORVIK 7 MAX besteht z.B. aus folgenden Einzelmodulen:
- BASIS (Basismodul)
- MDE (Maschinendatenerfassung)
- BDE (Betriebsdatenerfassung)
- INST (Instandhaltung)
- ALARM (Alarmierung)
- DOK (Dokumentenmanagement)
- TNT (Traceability)
- PLAN (Feinplanung/Leitstand)
- LOG (Logistik)
- VIS (Visualisierung)
- PEP (Personaleinsatzplanung)
- MPZE (Personalzeiterfassung)
- DNC (Rezepturen/DNC)
- EM (Energiemonitoring)
Aufgabenstellung
Die modulare Struktur und der große Umfang an Modulen ist ein wichtiger Vorteil für unsere Kunden, da Sie nicht so schnell an Grenzen stoßen und sich dann unter Umständen eine weitere Insellösung (extra Software mit extra Datenbank ...) anschaffen müssen.
Wichtig ist, dass die einzelnen Module funktionell ineinandergreifen und alle auf die gleiche Datenbank zugreifen.
Es reicht wenn in der Grafik die Module nur mit er Abkürzung, also z.B. MDE bezeichnet werden. Für den ersten Entwurf können auch Platzhalter genutzt werden.
Der Betrachter sollte aus der Grafik auf den ersten Blick erkennen:
- umfängliches MES
- modular strukturiert
- Funktionsmodule step-by-step erweiterbar
Für die Umsetzung naheliegend wären Puzzle-Steine, Stapolos, ... muss aber nicht.

```html
<!DOCTYPE html>
<html lang="de">
<head>
<meta charset="utf-8">
<title>MES Module</title>
<link rel="stylesheet" href="https://fonts.googleapis.com/css2?family=Source+Sans+3:wght@400;700&display=swap">
<style>
  :root {
    --bg-center: #ffffff;
    --bg-edge: #d6dadd;
    --hex-frame: #ffffff;
    --label: #ffffff;
  }
  html, body { margin: 0; padding: 0; overflow: hidden; }
  body { width: 1200px; height: 1200px; }
  .module-map {
    display: block;
    width: 1200px;
    height: 1200px;
    background: radial-gradient(circle at 50% 45%, var(--bg-center) 0%, #eef0f1 45%, var(--bg-edge) 100%);
    font-family: "Source Sans 3", sans-serif;
  }
  .hex-frame { fill: var(--hex-frame); filter: drop-shadow(0 6px 7px rgba(0,0,0,.22)); }
  .hex-head { fill: var(--dark); }
  .hex-body { fill: var(--light); }
  .module-code { fill: var(--label); font-weight: 700; font-size: 35px; text-anchor: middle; }
  .module-name { fill: var(--label); font-weight: 400; font-size: 16px; text-anchor: middle; }
  .badge-ring { fill: #ffffff; }
  .badge-inner { fill: var(--dark); opacity: .85; }
</style>
</head>
<body>
<svg class="module-map" viewBox="0 0 1240 1240" xmlns="http://www.w3.org/2000/svg">
  <defs>
    <polygon id="hex-outer" points="0,-150 130,-75 130,75 0,150 -130,75 -130,-75"/>
    <clipPath id="hex-inner-clip">
      <polygon points="0,-123.5 107,-61.75 107,61.75 0,123.5 -107,61.75 -107,-61.75"/>
    </clipPath>
    <g id="hex-tile">
      <use href="#hex-outer" class="hex-frame"/>
      <g clip-path="url(#hex-inner-clip)">
        <rect class="hex-body" x="-110" y="-4" width="220" height="130"/>
        <rect class="hex-head" x="-110" y="-126" width="220" height="122"/>
      </g>
      <circle class="badge-ring" cx="0" cy="51" r="46"/>
    </g>
  </defs>

  <g class="module" transform="translate(197,254)" style="--dark:#f9b000;--light:#fbc23f">
    <use href="#hex-tile"/>
    <text class="module-code" y="-48">BDE</text>
    <text class="module-name" y="-24">Betriebsdatenerfassung</text>
    <circle class="badge-inner" cy="51" r="40" role="img" aria-label="Symbol Betriebsdaten"/>
  </g>
  <g class="module" transform="translate(480,254)" style="--dark:#ef7d00;--light:#f29d3f">
    <use href="#hex-tile"/>
    <text class="module-code" y="-51">INST</text>
    <text class="module-name" y="-27">Instandhaltung</text>
    <circle class="badge-inner" cy="51" r="40" role="img" aria-label="Symbol Instandhaltung"/>
  </g>
  <g class="module" transform="translate(763,254)" style="--dark:#e84e0f;--light:#ec7a3c">
    <use href="#hex-tile"/>
    <text class="module-code" y="-51">ALARM</text>
    <text class="module-name" y="-27">Alarmierung</text>
    <circle class="badge-inner" cy="51" r="40" role="img" aria-label="Symbol Alarmierung"/>
  </g>
  <g class="module" transform="translate(1047,254)" style="--dark:#e2001a;--light:#e65136">
    <use href="#hex-tile"/>
    <text class="module-code" y="-48">DOK</text>
    <text class="module-name" y="-24">Dokumentenmanagement</text>
    <circle class="badge-inner" cy="51" r="40" role="img" aria-label="Symbol Dokumente"/>
  </g>

  <g class="module" transform="translate(335,497)" style="--dark:#b5cc18;--light:#c8d85e">
    <use href="#hex-tile"/>
    <text class="module-code" y="-45">MDE</text>
    <text class="module-name" y="-21">Maschinendatenerfassung</text>
    <circle class="badge-inner" cy="51" r="40" role="img" aria-label="Symbol Maschinendaten"/>
  </g>
  <g class="module" transform="translate(618,497)" style="--dark:#c0d1db;--light:#cbd9e1">
    <use href="#hex-tile"/>
    <text class="module-code" y="-50">BASIS</text>
    <text class="module-name" y="-26">Basismodul</text>
    <circle class="badge-inner" cy="51" r="40" role="img" aria-label="Symbol Basismodul"/>
  </g>
  <g class="module" transform="translate(901,497)" style="--dark:#009a36;--light:#4faa57">
    <use href="#hex-tile"/>
    <text class="module-code" y="-45">TNT</text>
    <text class="module-name" y="-21">Traceability</text>
    <circle class="badge-inner" cy="51" r="40" role="img" aria-label="Symbol Traceability"/>
  </g>

  <g class="module" transform="translate(197,745)" style="--dark:#7cc3ea;--light:#9dd2f0">
    <use href="#hex-tile"/>
    <text class="module-code" y="-45">PEP</text>
    <text class="module-name" y="-21">Personaleinsatzplanung</text>
    <circle class="badge-inner" cy="51" r="40" role="img" aria-label="Symbol Personaleinsatz"/>
  </g>
  <g class="module" transform="translate(480,745)" style="--dark:#2a93cf;--light:#68a9d7">
    <use href="#hex-tile"/>
    <text class="module-code" y="-45">VIS</text>
    <text class="module-name" y="-21">Visualisierung</text>
    <circle class="badge-inner" cy="51" r="40" role="img" aria-label="Symbol Visualisierung"/>
  </g>
  <g class="module" transform="translate(763,745)" style="--dark:#0e5aa7;--light:#4574b3">
    <use href="#hex-tile"/>
    <text class="module-code" y="-45">EM</text>
    <text class="module-name" y="-21">Energiemonitoring</text>
    <circle class="badge-inner" cy="51" r="40" role="img" aria-label="Symbol Energie"/>
  </g>
  <g class="module" transform="translate(1047,745)" style="--dark:#13296b;--light:#2d3f78">
    <use href="#hex-tile"/>
    <text class="module-code" y="-48">PLAN</text>
    <text class="module-name" y="-24">Feinplanung/Leitstand</text>
    <circle class="badge-inner" cy="51" r="40" role="img" aria-label="Symbol Feinplanung"/>
  </g>

  <g class="module" transform="translate(335,990)" style="--dark:#b8348a;--light:#c468a5">
    <use href="#hex-tile"/>
    <text class="module-code" y="-45">MPZE</text>
    <text class="module-name" y="-21">Personalzeiterfassung</text>
    <circle class="badge-inner" cy="51" r="40" role="img" aria-label="Symbol Zeiterfassung"/>
  </g>
  <g class="module" transform="translate(618,990)" style="--dark:#6e2d72;--light:#8a5689">
    <use href="#hex-tile"/>
    <text class="module-code" y="-45">DNC</text>
    <text class="module-name" y="-21">Rezepturen/DNC</text>
    <circle class="badge-inner" cy="51" r="40" role="img" aria-label="Symbol Rezepturen"/>
  </g>
  <g class="module" transform="translate(901,990)" style="--dark:#362a63;--light:#5d4a80">
    <use href="#hex-tile"/>
    <text class="module-code" y="-45">LOG</text>
    <text class="module-name" y="-21">Logistik</text>
    <circle class="badge-inner" cy="51" r="40" role="img" aria-label="Symbol Logistik"/>
  </g>
</svg>
</body>
</html>
```